Mobile Optometry needs descriptive brochure and business cards for patients

I need a brochure design and business cards for a new optometry service that brings full ocular examination, refraction, and spectacle dispensing to the patient in need.
I will mainly be working out of senior homes so it needs to be very legible NO SMALL PRINT, CLEAR, CONSCIENCE.
The final design needs to incorporate the logo and colouring that was just selected from a previous project. I will add this file as soon as I get the final changes back from the designer.

Here is what I would like in the broacher. I don't have a fax number, website address, email address set up yet but have room for this.

Note: I have attached the logo I selected for the company. I may not have attached the most detailed version but this will give you an idea of colouring and style. I will upload the proper image soon.

Routine eye examinations are crucial for early detection of diseases of the eye and effects of systemic conditions for everybody. As we age we are at higher risk of vision loss due to Glaucoma, Age-related Macular Degeneration, Diabetic or Hypertensive Retinopathy, Cataracts and many other diseases.

During your complete ocular visual assessment you will be screened for all conditions that may be affecting you as well as treat any issues you may be suffering from. Common treatable complaints: Dry eyes, Watery eyes, Burning, Itching, Difficulty reading small print, Reduced distance vision, Glare, Light sensitiveness, and difficulty performing hobbies.

Here is what your complete examination includes

Step 1: Appointment Request
-Call
-Email
-Phone
-Fax

Step 2: Welcome form
-Patient Name, DOB, Veltmore Care Plan number
-List current medications, allergies
-Current Visual difficulties
-Previous spectacle prescription (if available)

Step 3: Ocular Visual Assessment and Discussion of Results
-History & Symptoms
-Refraction
-Dilation and thorough ocular/retinal screening
-Spectacle or magnifier dispense if required
-Ophthalmologist or medical practitioner referral if required

Step 4: Dispense and Delivery
-Return to fit custom made glasses
-Demonstrate use low vision device
-Discuss any questions/treatments/referrals
Updates

I have just increased the budget. I am running out of time and want some good designs. I want a modern, clean and clear product. Please submit, points for originality.

Target Market(s)

The target audience is Professionals, managers, senior care facilities, families. I want something clean and easy to read. I want something modern but not trendy and something that appeals to the masses.

Industry/Entity Type

Medical

Font styles to use
Sans Serif

Requirements
Must have
• easy to read
bright
professional
Contact information on the last page
Nice to have
• order of services layer out nicely. Try a version with clearly defined steps. Step 1. Step 2. Step 3. Could be multiple broachers that are packaged together.
Should not have
• cartoony
serif fonts (please use font that is in logo)

```html
<!DOCTYPE html>
<html lang="en">
<head>
<meta charset="utf-8">
<title>ClearPath Eye Care – Mobile Optometry Flyer</title>
<link href="https://fonts.googleapis.com/css2?family=Lato:wght@400&family=Open+Sans:wght@400;600&family=PT+Sans:wght@700&display=swap" rel="stylesheet">
<style>
  :root {
    --green-light: #86cc12;
    --green-dark: #5c9d0a;
    --blue: #1f86c2;
    --blue-light: #41ade6;
    --panel-light: #f7f7f7;
    --panel-grey: #e4e4e4;
    --ink: #3a3a3a;
    --brand-ink: #555555;
    --white: #ffffff;
  }
  html, body {
    margin: 0;
    padding: 0;
    width: 1200px;
    height: 797px;
    overflow: hidden;
    background: #ffffff;
  }
  .flyer {
    position: relative;
    width: 1200px;
    height: 797px;
    overflow: hidden;
  }
  .flyer-art {
    position: absolute;
    inset: 0;
    width: 1200px;
    height: 797px;
  }
  .contact {
    position: absolute;
    left: 0;
    top: 52px;
    width: 600px;
    text-align: center;
    color: var(--white);
    font-family: "Lato", sans-serif;
    font-size: 17.5px;
  }
  .contact-title {
    margin: 0 0 18px;
    font-family: "PT Sans", sans-serif;
    font-weight: 700;
    font-size: 33px;
    letter-spacing: 0.5px;
    color: var(--ink);
    text-shadow: 0 1px 0 rgba(255,255,255,0.35);
  }
  .contact-list {
    list-style: none;
    margin: 0;
    padding: 0;
    line-height: 29.5px;
  }
  .contact-list li { margin: 0; }
  .contact-icon {
    width: 16px;
    height: 16px;
    vertical-align: -2px;
    margin-right: 10px;
    fill: var(--white);
  }
  .contact-indent { padding-left: 34px; }
  .headline {
    position: absolute;
    left: 600px;
    top: 40px;
    width: 590px;
    margin: 0;
    text-align: center;
    font-family: "Open Sans", sans-serif;
    font-weight: 600;
    font-size: 64px;
    letter-spacing: 1px;
    line-height: 1;
    color: var(--blue-light);
    text-shadow: 0 2px 3px rgba(0,0,0,0.25);
  }
  .brand {
    position: absolute;
    left: 620px;
    top: 676px;
    width: 580px;
    text-align: center;
    font-family: "Open Sans", sans-serif;
  }
  .brand-name {
    margin: 0;
    font-size: 40px;
    font-weight: 600;
    color: var(--brand-ink);
    line-height: 1;
  }
  .brand-dot {
    display: inline-block;
    width: 22px;
    height: 22px;
    border-radius: 50%;
    background: var(--green-dark);
    margin-right: 12px;
    vertical-align: 3px;
  }
  .brand-tagline {
    margin: 12px 0 0;
    font-size: 17px;
    font-weight: 400;
    letter-spacing: 1.5px;
    color: var(--ink);
  }
  .brand-tagline::before,
  .brand-tagline::after {
    content: "";
    display: inline-block;
    width: 52px;
    height: 2px;
    background: var(--blue-light);
    vertical-align: 5px;
    margin: 0 10px;
  }
</style>
</head>
<body>
<main class="flyer">
  <svg class="flyer-art" viewBox="0 0 1200 797" xmlns="http://www.w3.org/2000/svg">
    <defs>
      <linearGradient id="greenPanel" x1="0" y1="0" x2="1" y2="1">
        <stop offset="0" stop-color="#8fd414"/>
        <stop offset="1" stop-color="#5c9d0a"/>
      </linearGradient>
      <linearGradient id="lightPanel" x1="0" y1="0" x2="0" y2="1">
        <stop offset="0" stop-color="#ffffff"/>
        <stop offset="1" stop-color="#dedede"/>
      </linearGradient>
      <linearGradient id="chartPhoto" x1="0" y1="0" x2="1" y2="1">
        <stop offset="0" stop-color="#d9d9d9"/>
        <stop offset="0.5" stop-color="#f2f2f2"/>
        <stop offset="1" stop-color="#c9b9a8"/>
      </linearGradient>
      <linearGradient id="manPhoto" x1="0" y1="0" x2="0" y2="1">
        <stop offset="0" stop-color="#c8c8c8"/>
        <stop offset="0.5" stop-color="#d8b49a"/>
        <stop offset="1" stop-color="#b9c8dc"/>
      </linearGradient>
      <linearGradient id="womanPhoto" x1="0" y1="0" x2="0" y2="1">
        <stop offset="0" stop-color="#4a3326"/>
        <stop offset="0.5" stop-color="#caa088"/>
        <stop offset="1" stop-color="#e4e4e4"/>
      </linearGradient>
      <clipPath id="photoArea">
        <path d="M134,815 C200,438 520,248 1200,215 L1200,797 L134,797 Z"/>
      </clipPath>
      <clipPath id="lowerArea">
        <path d="M518,803 C700,626 950,546 1200,536 L1200,797 Z"/>
      </clipPath>
    </defs>

    <!-- panels -->
    <rect class="panel-green" x="0" y="0" width="600" height="797" fill="url(#greenPanel)"/>
    <rect class="panel-light" x="600" y="0" width="600" height="797" fill="url(#lightPanel)"/>

    <!-- upper sweep bands -->
    <path class="band-white" d="M134,777 C200,400 520,210 1200,177 L1200,797 L134,797 Z" fill="#ffffff"/>
    <path class="band-green" d="M134,783 C200,406 520,216 1200,183 L1200,797 L134,797 Z" fill="#6fb80e"/>
    <path class="band-white" d="M134,799 C200,422 520,232 1200,199 L1200,797 L134,797 Z" fill="#ffffff"/>
    <path class="band-blue" d="M134,803 C200,426 520,236 1200,203 L1200,797 L134,797 Z" fill="var(--blue)"/>

    <!-- photo areas -->
    <g clip-path="url(#photoArea)">
      <rect role="img" aria-label="Photo of a smiling woman in glasses beside a blurred eye chart" x="0" y="150" width="600" height="647" fill="url(#chartPhoto)"/>
      <rect role="img" aria-label="Photo of a smiling man wearing glasses" x="600" y="150" width="280" height="647" fill="url(#manPhoto)"/>
      <rect role="img" aria-label="Photo of a smiling young woman adjusting her glasses" x="884" y="150" width="316" height="647" fill="url(#womanPhoto)"/>
      <rect class="photo-divider" x="880" y="150" width="4" height="647" fill="#ffffff"/>
    </g>

    <!-- lower sweep bands -->
    <path class="band-white" d="M518,781 C700,604 950,524 1200,514 L1200,797 Z" fill="#ffffff"/>
    <path class="band-blue" d="M518,787 C700,610 950,530 1200,520 L1200,797 Z" fill="var(--blue)"/>
    <path class="band-green" d="M518,795 C700,618 950,538 1200,528 L1200,797 Z" fill="#72ba0e"/>
    <g clip-path="url(#lowerArea)">
      <rect class="brand-area" x="500" y="500" width="700" height="297" fill="url(#lightPanel)"/>
      <rect class="corner-green" x="500" y="500" width="100" height="297" fill="#6fb80e"/>
    </g>
  </svg>

  <section class="contact">
    <h2 class="contact-title">CONTACT US</h2>
    <ul class="contact-list">
      <li>
        <svg class="contact-icon" viewBox="0 0 16 16"><path d="M8 1 L15 8 H13 V15 H9.5 V10.5 H6.5 V15 H3 V8 H1 Z"/></svg>Lorem ipsum dolor sit amet, consectetuer elit
      </li>
      <li class="contact-indent">suscipit lobortis nisl ut aliquip</li>
      <li>
        <svg class="contact-icon" viewBox="0 0 16 16"><path d="M1 5 C1 3 3 2 8 2 C13 2 15 3 15 5 V6.5 H11 V5 H5 V6.5 H1 Z M3 8 H13 L14 14 H2 Z"/></svg>123456789
      </li>
      <li>
        <svg class="contact-icon" viewBox="0 0 16 16"><path d="M1 6 L8 1 L15 6 V14 H1 Z M2.5 6.5 L8 10.5 L13.5 6.5 L8 2.8 Z"/></svg>loremipsum.net@clearpatheyecare.com
      </li>
      <li>
        <svg class="contact-icon" viewBox="0 0 16 16"><circle cx="8" cy="8" r="6.5" fill="none" stroke="#fff" stroke-width="1.4"/><path d="M1.5 8 H14.5 M8 1.5 V14.5" stroke="#fff" stroke-width="1.2"/><ellipse cx="8" cy="8" rx="3" ry="6.5" fill="none" stroke="#fff" stroke-width="1.2"/></svg>www.loremipsum.net
      </li>
    </ul>
  </section>

  <h1 class="headline">SEE YOUR BEST</h1>

  <section class="brand">
    <p class="brand-name"><span class="brand-dot"></span>ClearPath Eye Care</p>
    <p class="brand-tagline">MOBILE OPTOMETRY</p>
  </section>
</main>
</body>
</html>
```